Milo's Sweet Harbor Package Design

A logo has already been made and now i need to incorporate that logo into a package design. Milo's Sweet Harbor products will be sold in retail stores and its package should appeal to both adults and children. Milo's Sweet Harbor sells candy, nuts and other snacks. Files attached will be logo files and pictures of similar package. Please refer to the files for package design. The physical package consists of a printed card (5.75 inches X 4 inches) and a plastic bag. The card is folded over the plastic bag, sealed and hole punched. The design on the card(5.75 inches X 4 inches) should consist of the logo, price(in this case it is $1.99 however it will vary for other products) and product type (in this case its apple(however it will change for other products). On the "back side"(the card is folded down the middle over the plastic and the top of the card becomes the back side, notice how in the example the top half is upside down, this is correct) should include nutrition facts, ingredients, a UPC barcode and the company information(again these vary depending on the product except for the company information that will be same for all products. Company info - "Packaged & Distributed By: Brevik Treats Supply
7142 Larchmont Ave Suite 208 Sterling Heights, Michigan 48592 586-555-0173"

TO WHOEVER WINS THE CONTEST WE WILL COMMISSION YOU TO USE THE SAME DESIGN AND ADD THE NECESSARY INFORMATION(upc, ingredients list, nutritional facts, etc) FOR THE MULTIPLE FLAVORS THAT WE WILL BE PRODUCING UNDER THE Milo's Sweet Harbor BRAND.

```html
<!DOCTYPE html>
<html lang="en">
<head>
<meta charset="utf-8">
<title>Milo's Sweet Harbor – Apple Header Card</title>
<link rel="stylesheet" href="https://fonts.googleapis.com/css2?family=Archivo:wght@400;700;900&family=Cabin:wght@400;700&family=Lilita+One&display=swap">
<style>
  :root{
    --bg:#f1f1f1;
    --card-white:#ffffff;
    --ink:#111111;
    --pink:#ef4a7e;
    --pink-deep:#d23f6e;
    --lime:#cddc2a;
    --dots:#e6918c;
    --cream:#fbf4e2;
    --red:#d8202a;
    --orange:#f7901e;
    --yellow:#f8e21c;
    --green:#8cc63f;
    --blue:#2e9ad6;
    --indigo:#3b3f9c;
    --purple:#8e44d1;
  }
  *{box-sizing:border-box;margin:0;padding:0}
  html,body{width:1198px;height:1200px;overflow:hidden;background:var(--bg)}
  .stage{position:relative;width:1198px;height:1200px}
  .header-card{
    position:absolute;left:99px;top:252px;width:1000px;height:695px;
    box-shadow:0 6px 18px rgba(0,0,0,.18);
  }
  /* back panel – printed upside down so it reads correctly once folded */
  .back-panel{
    position:absolute;left:0;top:0;width:1000px;height:347.5px;
    background:var(--card-white);transform:rotate(180deg);
    font-family:"Cabin",sans-serif;color:var(--ink);
  }
  .nutrition-facts{
    position:absolute;left:23px;top:27px;width:200px;height:294px;
    border:1px solid var(--ink);padding:4px 5px;
    font-family:"Archivo",sans-serif;font-size:7.4px;line-height:1.25;
  }
  .nf-title{font-weight:900;font-size:18px;letter-spacing:.5px;line-height:1.1}
  .nf-row{display:flex;justify-content:space-between;border-top:.6px solid var(--ink);padding:1px 0}
  .nf-row.indent{padding-left:8px}
  .nf-row.indent2{padding-left:16px}
  .nf-bold{font-weight:700}
  .nf-rule-thick{border-top:7px solid var(--ink);margin-top:2px}
  .nf-rule-mid{border-top:3px solid var(--ink)}
  .nf-serving{display:flex;justify-content:space-between;font-weight:700;font-size:9.5px}
  .nf-calories{display:flex;justify-content:space-between;align-items:flex-end;font-weight:900;font-size:16px;line-height:1}
  .nf-calories .amt{font-size:22px}
  .nf-dv{text-align:right;font-size:6px;font-weight:700;padding:1px 0}
  .nf-foot{font-size:6px;line-height:1.3;padding-top:3px}
  .back-flavor{
    position:absolute;left:500px;top:92px;transform:translateX(-50%);
    font-family:"Archivo",sans-serif;font-weight:700;font-size:19px;
  }
  .ingredients{
    position:absolute;left:797px;top:20px;transform:translateX(-50%);
    width:360px;text-align:center;font-size:20px;line-height:28px;
  }
  .ingredients h2{font-family:"Archivo",sans-serif;font-weight:900;font-size:20px;letter-spacing:.5px;line-height:28px}
  .upc-space{position:absolute;left:714px;top:206px;width:169px;height:88px;border:1.5px solid var(--ink)}
  .distributor-line{
    position:absolute;left:500px;top:303px;transform:translateX(-50%);
    font-size:16px;white-space:nowrap;
  }
  /* front panel */
  .front-panel{position:absolute;left:0;top:347.5px;width:1000px;height:347.5px;overflow:hidden;background:var(--lime)}
  .front-pink{position:absolute;left:0;top:0;width:500px;height:100%;background:var(--pink)}
  .dot-strip{position:absolute;left:500px;top:0;width:65px;height:100%;
    background:linear-gradient(180deg,var(--dots),#eba07f)}
  .rainbow{position:absolute;left:0;top:0}
  .brand-name{
    position:absolute;left:94px;top:110px;width:271px;text-align:center;
    font-family:"Lilita One",sans-serif;font-size:44px;line-height:48px;color:#ffffff;
  }
  .price-tag{
    position:absolute;left:690px;top:41px;width:191px;height:117px;border-radius:50%;
    background:var(--cream);border:5px solid var(--red);
    display:flex;align-items:center;justify-content:center;
    font-family:"Archivo",sans-serif;font-weight:900;font-size:50px;color:var(--red);letter-spacing:1px;
  }
  .flavor-name{
    position:absolute;left:618px;top:222px;
    font-family:"Lilita One",sans-serif;font-size:96px;line-height:1;color:#ffffff;
    -webkit-text-stroke:9px var(--pink);paint-order:stroke fill;letter-spacing:1px;
  }
</style>
</head>
<body>
<main class="stage">
  <article class="header-card">
    <section class="back-panel">
      <div class="nutrition-facts">
        <div class="nf-title">Nutrition Facts</div>
        <div style="border-top:.6px solid var(--ink);padding-top:1px">6 servings per container</div>
        <div class="nf-serving"><span>Serving size</span><span>10 pcs (10g)</span></div>
        <div class="nf-rule-thick"></div>
        <div class="nf-bold" style="font-size:6.5px">Amount Per Serving</div>
        <div class="nf-calories"><span>Calories</span><span class="amt">110</span></div>
        <div class="nf-rule-mid" style="margin-top:2px"></div>
        <div class="nf-dv">% Daily Value*</div>
        <div class="nf-row"><span><b>Total Fat</b> 2.5g</span><b>3%</b></div>
        <div class="nf-row indent"><span>Saturated Fat 1g</span><b>5%</b></div>
        <div class="nf-row indent"><span><i>Trans</i> Fat 0g</span><span></span></div>
        <div class="nf-row"><span><b>Sodium</b> 10mg</span><b>0%</b></div>
        <div class="nf-row"><span><b>Total Carbohydrate</b> 22g</span><b>8%</b></div>
        <div class="nf-row indent"><span>Dietary Fiber 0g</span><b>0%</b></div>
        <div class="nf-row indent"><span>Total Sugars 16g</span><span></span></div>
        <div class="nf-row indent2"><span>Includes 0g Added Sugars</span><b>0%</b></div>
        <div class="nf-row"><span><b>Protein</b> 0g</span><b>0%</b></div>
        <div class="nf-rule-thick" style="margin-top:0"></div>
        <div class="nf-foot">Not a significant source of cholesterol, vitamin D, calcium, iron, and potassium</div>
        <div class="nf-foot" style="border-top:.6px solid var(--ink)">* The % Daily Value (DV) tells you how much a nutrient in a serving of food contributes to a daily diet. 2,000 calories a day is used for general nutrition advice.</div>
      </div>
      <div class="back-flavor">Apple</div>
      <div class="ingredients">
        <h2>INGREDIENTS:</h2>
        <p>Sugar, Corn Syrup, Palm Oil,<br>Condensed Skim Milk, Whey<br>Malic Acid, Artificial Flavors,<br>Soy Lecithin, Artificial Colors<br>(Including FD&amp;C Yellow 5, Blue 1)</p>
      </div>
      <div class="upc-space"></div>
      <p class="distributor-line">Produced &amp; Distributed by Milo's Sweet Harbor</p>
    </section>

    <section class="front-panel">
      <div class="front-pink"></div>
      <div class="dot-strip" role="img" aria-label="Vertical strip of pink polka dots on yellow"></div>
      <svg class="rainbow" width="1000" height="348" viewBox="0 0 1000 348" aria-hidden="true">
        <path fill="var(--red)"    d="M330 270 C560 260 700 215 1000 173 L1000 198 C700 240 560 280 330 277 Z"/>
        <path fill="var(--orange)" d="M330 277 C560 280 700 240 1000 198 L1000 223 C700 265 560 300 330 284 Z"/>
        <path fill="var(--yellow)" d="M330 284 C560 300 700 265 1000 223 L1000 248 C700 290 560 320 330 291 Z"/>
        <path fill="var(--green)"  d="M330 291 C560 320 700 290 1000 248 L1000 273 C700 315 560 340 330 298 Z"/>
        <path fill="var(--blue)"   d="M330 298 C560 340 700 315 1000 273 L1000 298 C700 340 560 360 330 305 Z"/>
        <path fill="var(--indigo)" d="M330 305 C560 360 700 340 1000 298 L1000 323 C700 365 560 380 330 312 Z"/>
        <path fill="var(--purple)" d="M330 312 C560 380 700 365 1000 323 L1000 348 L330 348 Z"/>
      </svg>
      <div class="brand-name">Milo's<br>Sweet Harbor</div>
      <div class="price-tag">$1.99</div>
      <div class="flavor-name">Apple</div>
    </section>
  </article>
</main>
</body>
</html>
```